New business card for civil engineering company - "Keystone Audit"

We need a business card designed for our new structural engineering company.

The company name is "Keystone Audit" logo files attached.

We would like the following:
* Two-sided card
* Simple design

Information to be placed on the card:
Name - Marcus Dellow
Job Title - Director / Structural Engineer
Credentials - BEng(Hons), CPEng, CMengNZ, IntPE(NZ)
Email - marcus.dellow@keystoneaudit.co.nz
mobile - 0219364058
website - www.keystoneaudit.co.nz

```html
<!DOCTYPE html>
<html lang="en">
<head>
<meta charset="utf-8">
<title>Keystone Audit — Business Card</title>
<link rel="stylesheet" href="https://fonts.googleapis.com/css2?family=Carlito:wght@400;700&display=swap">
<style>
  :root {
    --stage: #3a3c40;
    --stage-edge: #23252a;
    --card-dark: #1c1c1e;
    --card-light: #ffffff;
    --brand-blue: #1b73c0;
    --icon-blue: #2a86cf;
    --ink: #3b3b3d;
    --rule: #6a6a6a;
    --on-dark: #f2f2f2;
  }
  * { margin: 0; padding: 0; box-sizing: border-box; }
  html, body { width: 1200px; height: 874px; overflow: hidden; }
  body {
    background: radial-gradient(ellipse at 40% 35%, var(--stage) 0%, var(--stage-edge) 100%);
    font-family: "Carlito", "Calibri", sans-serif;
    position: relative;
  }
  .card {
    position: absolute;
    width: 600px;
    height: 343px;
    border-radius: 26px;
    box-shadow: 0 18px 40px rgba(0,0,0,0.45);
    overflow: hidden;
  }
  /* Back side */
  .card--back {
    left: 70px; top: 70px;
    background: var(--card-dark);
    display: flex; align-items: center; justify-content: center;
  }
  .brand {
    display: flex; align-items: center; gap: 14px;
    font-size: 40px; font-weight: 400; letter-spacing: 3px;
    text-transform: uppercase;
  }
  .brand__mark { width: 22px; height: 22px; }
  .card--back .brand { color: var(--on-dark); }
  .card--back .brand__mark { background: var(--on-dark); }

  /* Front side */
  .card--front {
    left: 530px; top: 460px;
    background: var(--card-light);
    display: grid;
    grid-template-columns: 250px 1px 1fr;
  }
  .front__brand {
    display: flex; align-items: center; justify-content: center;
  }
  .front__brand .brand {
    font-size: 22px; letter-spacing: 1.5px; gap: 10px;
    color: var(--brand-blue);
  }
  .front__brand .brand__mark { width: 14px; height: 14px; background: var(--brand-blue); }
  .divider {
    background: linear-gradient(to bottom, transparent, var(--rule) 15%, var(--rule) 85%, transparent);
    margin: 36px 0;
  }
  .details { padding: 52px 24px 0 34px; color: var(--ink); }
  .details__name {
    font-size: 36px; font-weight: 700; color: var(--brand-blue);
    line-height: 1.05;
  }
  .details__title, .details__creds {
    font-size: 16px; line-height: 1.3;
  }
  .details__title { margin-top: 6px; }
  .contact { list-style: none; margin-top: 34px; }
  .contact__item {
    display: flex; align-items: center; gap: 10px;
    font-size: 15.5px; line-height: 1.55;
  }
  .contact__icon { width: 14px; height: 14px; flex: none; }
</style>
</head>
<body>
  <section class="card card--back" aria-label="Card back">
    <div class="brand"><span class="brand__mark"></span>Keystone Audit</div>
  </section>

  <section class="card card--front" aria-label="Card front">
    <div class="front__brand">
      <div class="brand"><span class="brand__mark"></span>Keystone Audit</div>
    </div>
    <div class="divider"></div>
    <div class="details">
      <h1 class="details__name">Marcus Dellow</h1>
      <p class="details__title">Director / Structural Engineer</p>
      <p class="details__creds">BEng(Hons), CPEng, CMengNZ<br>IntPE(NZ)</p>
      <ul class="contact">
        <li class="contact__item">
          <svg class="contact__icon" viewBox="0 0 24 24" aria-hidden="true"><path fill="var(--icon-blue)" d="M6.6 10.8a15 15 0 0 0 6.6 6.6l2.2-2.2c.3-.3.7-.4 1-.2 1.1.4 2.3.6 3.6.6.6 0 1 .4 1 1V20c0 .6-.4 1-1 1A17 17 0 0 1 3 4c0-.6.4-1 1-1h3.5c.6 0 1 .4 1 1 0 1.3.2 2.5.6 3.6.1.3 0 .7-.2 1z"/></svg>
          0219364058
        </li>
        <li class="contact__item">
          <svg class="contact__icon" viewBox="0 0 24 24" aria-hidden="true"><rect x="2" y="5" width="20" height="14" rx="1.5" fill="none" stroke="var(--icon-blue)" stroke-width="2.4"/><path d="M3 6l9 7 9-7" fill="none" stroke="var(--icon-blue)" stroke-width="2.4"/></svg>
          marcus.dellow@keystoneaudit.co.nz
        </li>
        <li class="contact__item">
          <svg class="contact__icon" viewBox="0 0 24 24" aria-hidden="true"><circle cx="12" cy="12" r="10" fill="none" stroke="var(--icon-blue)" stroke-width="2.4"/><path d="M2 12h20M12 2c3 3 3 17 0 20M12 2c-3 3-3 17 0 20" fill="none" stroke="var(--icon-blue)" stroke-width="1.8"/></svg>
          www.keystoneaudit.co.nz
        </li>
      </ul>
    </div>
  </section>
</body>
</html>
```